Marketing , Sales and Distribution Website

This website/this business is specifically to start an international marketing, sales and distribution business - no more than 5 pages - one page design with supporting pages, a strong "call to action" design - lead generation design - Modern - can be easily upgraded.

Target Market(s)

Industrial, engineering, Art, technology, food products, fashion and accessories

Industry/Entity Type

Marketing

Coding

Coded - Design and coding required

Font styles to use
Sans Serif

Requirements
Must have
• user friendly. Fast upload time - space for content. Most have strategic "call to action" lead generation opportunities - space for video, links to social media. room for articles, blogs and upcoming tradeshows - modern interactive website - easy to upgrade in the future. Lastly a link or Tab to a one page site dedicated to mobile marketing subscriptions
Nice to have
• Client login area - backend CRM integration - Hubspot
• I am open to suggestions to make this site attractive for companies who import/export goods - or generate leads of companies who wish to import/export their products to the USA - a lot of this information is in the attachment.

```html
<!DOCTYPE html>
<html lang="en">
<head>
<meta charset="utf-8">
<title>Norvale Marketing</title>
<link href="https://fonts.googleapis.com/css2?family=Bebas+Neue&family=Roboto:wght@300;400;500&display=swap" rel="stylesheet">
<style>
:root{
  --navy:#2b3a7c;
  --navy-deep:#233068;
  --sky:#9db4e1;
  --sky-soft:#a9bde6;
  --title-light:#98b0e0;
  --ink:#26336e;
  --text:#555b6b;
  --muted:#8a8f9c;
  --card:#f1f1f3;
  --white:#ffffff;
}
*{margin:0;padding:0;box-sizing:border-box}
html,body{width:1200px;height:3629px;overflow:hidden}
body{position:relative;font-family:"Roboto",Arial,sans-serif;color:var(--text);background:var(--white)}
.abs{position:absolute}
a{color:inherit;text-decoration:none}
.btn{position:absolute;display:flex;align-items:center;justify-content:center;background:var(--navy);color:var(--white);font-size:21px;font-weight:400;border-radius:3px;letter-spacing:.3px;white-space:nowrap}
.ph{position:absolute}
.section-title{position:absolute;left:0;width:1200px;text-align:center;font-size:42px;font-weight:400;color:var(--ink);letter-spacing:.5px}
.section-title .lite{color:var(--title-light)}

/* header */
.site-header{left:0;top:0;width:1200px;height:135px;background:var(--white)}
.brand{left:80px;top:12px;height:109px;display:flex;align-items:center;gap:14px;font-size:26px;font-weight:500;color:var(--navy)}
.brand .mark{width:24px;height:24px;background:var(--navy)}
.topbar{right:80px;top:12px;display:flex;gap:30px;font-size:18px;color:var(--ink);align-items:center}
.topbar span{display:flex;align-items:center;gap:9px}
.main-nav{top:65px;left:0;width:1200px;height:51px;font-size:17px;color:var(--ink)}
.main-nav a{position:absolute;top:0;height:51px;display:flex;align-items:center;justify-content:center;letter-spacing:.4px;white-space:nowrap}
.main-nav a.active{background:var(--navy);color:var(--white);border-radius:3px;width:100px}

/* hero */
.hero{left:0;top:135px;width:1200px;height:552px;background:linear-gradient(180deg,#c7ccd6 0%,#9ea7b9 45%,#6f7c98 100%)}
.hero h1{position:absolute;left:0;top:178px;width:1200px;text-align:center;font-family:"Bebas Neue","Arial Narrow",sans-serif;font-weight:400;font-size:96px;line-height:1;color:#111;letter-spacing:1px}
.hero p{position:absolute;left:0;top:280px;width:1200px;text-align:center;font-size:20px;line-height:24px;color:#111}
.hero .btn{left:506px;top:332px;width:188px;height:56px}
.slide-arrow{position:absolute;top:249px;width:48px;height:48px;border:2px solid #8a8f99;border-radius:50%;display:flex;align-items:center;justify-content:center}

/* welcome */
.welcome{left:0;top:687px;width:1200px;height:261px;background:var(--navy);color:var(--white);text-align:center}
.welcome h2{margin-top:54px;font-size:40px;font-weight:400;color:var(--title-light)}
.welcome h2 b{font-weight:400;color:var(--white)}
.welcome p{width:920px;margin:16px auto 0;font-size:14px;line-height:28px;color:#e6e9f3}
.welcome svg{margin-top:8px}

/* services */
.service{position:absolute;top:1079px;width:333px;height:481px}
.service .ph{left:0;top:0;width:333px;height:220px}
.service .body{position:absolute;left:0;top:220px;width:333px;height:261px;background:var(--sky);padding:22px 16px 0}
.service h3{font-size:21px;font-weight:400;color:var(--ink);margin-bottom:10px}
.service ul{list-style:none;font-size:13.5px;line-height:26px;color:#fff}
.service li{padding-left:16px;position:relative}
.service li::before{content:"";position:absolute;left:2px;top:11px;width:6px;height:6px;border-radius:50%;background:#fff}
.service .btn{left:16px;top:179px;width:165px;height:51px}

/* video */
.video{left:0;top:1621px;width:1200px;height:399px;background:linear-gradient(120deg,#3b4a8c 0%,#4c5d9f 50%,#34437f 100%)}
.video h2{position:absolute;left:0;top:84px;width:1200px;text-align:center;font-size:40px;font-weight:400;color:#fff}
.video h2 .lite{color:#b7c7ea}
.play{position:absolute;left:554px;top:171px}

/* cta band */
.cta{left:0;top:2020px;width:1200px;height:194px;background:var(--sky-soft)}
.cta h2{position:absolute;left:80px;top:42px;font-size:40px;font-weight:400;color:#fff}
.cta h2 b{font-weight:400;color:var(--ink)}
.cta p{position:absolute;left:80px;top:100px;width:760px;font-size:14.5px;line-height:27px;color:var(--ink)}
.cta p em{font-weight:500;text-decoration:underline}
.cta .btn{left:883px;top:70px;width:237px;height:56px}

/* ebook & news */
.col-title{position:absolute;font-size:40px;font-weight:400;color:var(--ink)}
.col-title .lite{color:var(--title-light)}
.divider-v{left:573px;top:2265px;width:2px;height:400px;background:linear-gradient(180deg,rgba(200,204,214,0) 0%,#d2d5dd 50%,rgba(200,204,214,0) 100%)}
.ebook-lead{left:227px;top:2380px;font-size:19px;line-height:26px;color:#222;width:300px}
.ebook-hint{left:227px;top:2444px;font-size:13.5px;color:#8aa2d6}
.ebook-text{left:80px;top:2515px;width:480px;font-size:13.5px;line-height:27px;color:var(--muted)}
.email-field{left:77px;top:2589px;width:310px;height:55px;background:#f0f1f3;border:1px solid #e0e2e7;display:flex;align-items:center;justify-content:space-between;padding:0 16px;font-size:14px;color:#555}
.subscribe{left:402px;top:2589px;width:145px;height:55px}
.news-item{position:absolute;left:622px;width:520px;height:106px}
.news-item .ph{left:0;top:0;width:96px;height:106px}
.news-item h4{position:absolute;left:125px;top:0;font-size:15.5px;font-weight:400;color:#222}
.news-item .date{position:absolute;left:125px;top:28px;font-size:14px;color:#333;display:flex;gap:9px;align-items:center}
.news-item p{position:absolute;left:125px;top:54px;width:400px;font-size:13.5px;line-height:25px;color:var(--muted)}
.view-all{left:619px;top:2589px;width:146px;height:55px}

/* blog */
.post{position:absolute;top:2811px;width:333px;height:443px;background:var(--card)}
.post .ph{left:0;top:0;width:333px;height:208px}
.post .day{position:absolute;left:0;top:0;width:77px;height:72px;background:var(--navy);color:#fff;text-align:center}
.post .day b{display:block;font-size:30px;font-weight:400;margin-top:6px}
.post .day span{font-size:13px}
.post h3{position:absolute;left:13px;top:236px;width:310px;font-size:15.5px;line-height:30px;font-weight:500;color:var(--ink)}
.post p{position:absolute;left:13px;top:304px;width:310px;font-size:13.5px;line-height:26px;color:var(--muted)}
.post .more{position:absolute;left:13px;top:396px;font-size:14px;color:var(--ink);display:flex;gap:4px;align-items:center}

/* footer */
.site-footer{left:0;top:3309px;width:1200px;height:320px;background:var(--navy-deep);color:#dfe4f2}
.foot-brand{position:absolute;left:108px;top:88px;font-size:22px;font-weight:500;color:#fff;display:flex;align-items:center;gap:10px;width:200px}
.foot-brand .mark{width:18px;height:18px;background:var(--sky)}
.social{position:absolute;top:183px;width:40px;height:40px;border-radius:50%;border:2px solid #c5d1ec;background:#5a6cae}
.foot-col{position:absolute;top:44px}
.foot-col h5{font-size:17px;font-weight:400;color:#fff;letter-spacing:.5px;margin-bottom:16px}
.foot-col li{list-style:none;font-size:14px;line-height:31px;color:#c9d2ea}
.foot-post{display:flex;gap:14px;margin-bottom:16px;width:220px}
.foot-post .ph{position:relative;width:50px;height:50px;border-radius:50%;flex:none}
.foot-post p{font-size:13.5px;line-height:20px;color:#e2e7f4}
.foot-post small{display:block;font-size:11px;color:#aab5d6}
.contact-row{display:flex;gap:14px;align-items:flex-start;font-size:14px;line-height:20px;margin-bottom:16px;color:#e2e7f4;width:260px}
.contact-row svg{flex:none;margin-top:2px}
.foot-rule{left:0;top:258px;width:1200px;height:1px;background:#3c4a86}
.copyright{left:0;top:282px;width:1200px;text-align:center;font-size:14px;color:#d5dbee}
</style>
</head>
<body>

<header class="site-header abs">
  <div class="brand abs"><span class="mark"></span>Norvale</div>
  <div class="topbar abs">
    <span><svg width="16" height="16" viewBox="0 0 16 16"><path d="M3 1l3 3-2 2c1 2 3 4 5 5l2-2 3 3-2 3C7 14 2 9 1 3z" fill="var(--ink)"/></svg>123-456-7890</span>
    <span><svg width="16" height="16" viewBox="0 0 16 16"><circle cx="8" cy="5" r="3.5" fill="var(--ink)"/><path d="M1 16c0-4 3-6 7-6s7 2 7 6z" fill="var(--ink)"/></svg>Client Login</span>
  </div>
  <nav class="main-nav abs">
    <a class="active" href="#" style="left:580px">HOME</a>
    <a href="#" style="left:722px;width:100px">MARKETING</a>
    <a href="#" style="left:860px;width:68px">SALES</a>
    <a href="#" style="left:958px;width:64px">NEWS</a>
    <a href="#" style="left:1050px;width:76px">E-BOOK</a>
  </nav>
</header>

<section class="hero abs" role="img" aria-label="Businessman in a suit and tie blended with a city skyline">
  <h1>NORVALE MARKETING</h1>
  <p>Product marketing, sales and distribution Full Service Product Marketing Firm</p>
  <a class="btn" href="#">CONTACT US</a>
  <span class="slide-arrow" style="left:17px"><svg width="14" height="18" viewBox="0 0 14 18"><path d="M10 2L3 9l7 7" stroke="#8a8f99" stroke-width="2" fill="none"/></svg></span>
  <span class="slide-arrow" style="left:1137px"><svg width="14" height="18" viewBox="0 0 14 18"><path d="M4 2l7 7-7 7" stroke="#8a8f99" stroke-width="2" fill="none"/></svg></span>
</section>

<section class="welcome abs">
  <h2>WELCOME TO <b>NORVALE MARKETING</b></h2>
  <p>Lorem Ipsum is simply dummy text of the printing and typesetting industry. Lorem Ipsum has been the industry's standard dummy text ever since the 1500s, when an unknown printer took a galley of type and scrambled it to make a type specimen book. It has survived not only five centuries, but also the leap into electronic typesetting, remaining essentially unchanged.</p>
  <svg width="20" height="20" viewBox="0 0 20 20"><path d="M3 4l7 6 7-6M3 10l7 6 7-6" stroke="#b9c8ea" stroke-width="2" fill="none"/></svg>
</section>

<h2 class="section-title" style="top:1003px"><span class="lite">OUR</span> SERVICES</h2>

<article class="service" style="left:77px">
  <div class="ph" role="img" aria-label="Hand drawing a rising line chart" style="background:linear-gradient(135deg,#e6e6e6,#b9b9bb)"></div>
  <div class="body">
    <h3>DISTRIBUTION</h3>
    <ul><li>Establish distribution in United States</li><li>On-self/Off Self marketing and management</li><li>Financing Assistance - Factoring Financing Available</li></ul>
    <a class="btn" href="#">CONTACT US</a>
  </div>
</article>
<article class="service" style="left:435px">
  <div class="ph" role="img" aria-label="Team meeting around a laptop" style="background:linear-gradient(135deg,#c9d7e6,#7c93b4)"></div>
  <div class="body">
    <h3>MARKETING</h3>
    <ul><li>On/Off shelf marketing, creating a demand branding, online marketing, social media management and marketing, SEM, PR etc.</li><li>Case studies product/market I've developed.</li></ul>
    <a class="btn" href="#">CONTACT US</a>
  </div>
</article>
<article class="service" style="left:791px">
  <div class="ph" role="img" aria-label="Chalk bar chart with rising arrow on a brick wall" style="background:linear-gradient(135deg,#efefef,#c4c4c4)"></div>
  <div class="body">
    <h3>SALES</h3>
    <ul><li>Trade shows assistance and promotions</li><li>Accompany on Sales trips</li><li>Target market analysis</li><li>Sales strategy development and planning</li></ul>
    <a class="btn" href="#">CONTACT US</a>
  </div>
</article>

<section class="video abs" role="img" aria-label="Hands holding a tablet with business charts">
  <h2><span class="lite">WATCH</span> A VIDEO</h2>
  <svg class="play" width="104" height="104" viewBox="0 0 104 104"><circle cx="52" cy="52" r="48" stroke="#fff" stroke-width="5" fill="none"/><path d="M40 30l34 22-34 22z" fill="#fff"/></svg>
</section>

<section class="cta abs">
  <h2>NORVALE <b>MARKETING</b></h2>
  <p>Lorem Ipsum is simply dummy text of the printing and typesetting industry. Lorem Ipsum has been the industry's standard dummy text ever since the 1500s, when an unknown printer <em>123 456 7890.</em></p>
  <a class="btn" href="#">BOOK APPOINTMENT</a>
</section>

<h2 class="col-title" style="left:80px;top:2270px"><span class="lite">DOWNLOAD</span> E-BOOK</h2>
<div class="ph" role="img" aria-label="E-book box cover" style="left:48px;top:2347px;width:146px;height:157px;background:linear-gradient(90deg,#1f2f6e,#3a4c92)"></div>
<p class="ebook-lead abs">Free Download in exchange for business information.</p>
<p class="ebook-hint abs">Enter your email to get access to my free e-book.</p>
<p class="ebook-text abs">Lorem Ipsum is simply dummy text of the printing and typesetting text of the industry Lorem Ipsum has been the industry's standard.</p>
<div class="email-field abs">Enter Your Email*<svg width="18" height="14" viewBox="0 0 18 14"><rect x="1" y="1" width="16" height="12" stroke="#555" stroke-width="1.5" fill="none"/><path d="M1 1l8 7 8-7" stroke="#555" stroke-width="1.5" fill="none"/></svg></div>
<a class="btn subscribe" href="#">SUBSCRIBE</a>

<div class="divider-v abs"></div>

<h2 class="col-title" style="left:617px;top:2270px"><span class="lite">LATEST</span> NEWS</h2>
<article class="news-item" style="top:2337px">
  <div class="ph" role="img" aria-label="Business handshake" style="background:linear-gradient(135deg,#d4dbe6,#7d8ba3)"></div>
  <h4>LOREM IPSUM IS SIMPLE DUMMY TEXT ?</h4>
  <span class="date"><svg width="14" height="14" viewBox="0 0 14 14"><rect x="1" y="2" width="12" height="11" fill="var(--ink)"/><rect x="2.5" y="5" width="9" height="6.5" fill="#fff"/></svg>10 Feb 2017</span>
  <p>Lorem Ipsum is simply dummy text of the printing and typesetting industry. Lorem Ipsum has been.</p>
</article>
<article class="news-item" style="top:2467px">
  <div class="ph" role="img" aria-label="Business partners shaking hands" style="background:linear-gradient(135deg,#dde3ec,#8593ab)"></div>
  <h4>LOREM IPSUM IS SIMPLE DUMMY TEXT?</h4>
  <span class="date"><svg width="14" height="14" viewBox="0 0 14 14"><rect x="1" y="2" width="12" height="11" fill="var(--ink)"/><rect x="2.5" y="5" width="9" height="6.5" fill="#fff"/></svg>10 Feb 2017</span>
  <p>Lorem Ipsum is simply dummy text of the printing and typesetting industry. Lorem Ipsum has been .</p>
</article>
<a class="btn view-all" href="#">VIEW ALL</a>

<h2 class="section-title" style="top:2730px"><span class="lite">LATEST</span> BLOG</h2>

<article class="post" style="left:77px">
  <div class="ph" role="img" aria-label="Hands reviewing printed charts on a desk" style="background:linear-gradient(135deg,#e9edf2,#a7b1c2)"></div>
  <div class="day"><b>10</b><span>February</span></div>
  <h3>LOREM IPSUM IS SIMPLE DUMMY TEXT OF PRINT &amp; TYPE ?</h3>
  <p>Lorem Ipsum is simply dummy text of the print - ing and typesetting industry. Lorem Ipsum has been the industry's standard dummy.</p>
  <a class="more" href="#">READ MORE...<svg width="12" height="10" viewBox="0 0 12 10"><path d="M1 1l4 4-4 4M6 1l4 4-4 4" stroke="var(--ink)" stroke-width="1.5" fill="none"/></svg></a>
</article>
<article class="post" style="left:434px">
  <div class="ph" role="img" aria-label="Business people meeting in an office" style="background:linear-gradient(135deg,#dfe3ea,#8e99ad)"></div>
  <div class="day"><b>10</b><span>February</span></div>
  <h3>LOREM IPSUM IS SIMPLE DUMMY TEXT OF PRINT &amp; TYPE ?</h3>
  <p>Lorem Ipsum is simply dummy text of the print - ing and typesetting industry. Lorem Ipsum has been the industry's standard dummy.</p>
  <a class="more" href="#">READ MORE...<svg width="12" height="10" viewBox="0 0 12 10"><path d="M1 1l4 4-4 4M6 1l4 4-4 4" stroke="var(--ink)" stroke-width="1.5" fill="none"/></svg></a>
</article>
<article class="post" style="left:790px">
  <div class="ph" role="img" aria-label="Businessman facing a digital data screen" style="background:linear-gradient(135deg,#6f8fb8,#1f3866)"></div>
  <div class="day"><b>10</b><span>February</span></div>
  <h3>LOREM IPSUM IS SIMPLE DUMMY TEXT OF PRINT &amp; TYPE ?</h3>
  <p>Lorem Ipsum is simply dummy text of the print - ing and typesetting industry. Lorem Ipsum has been the industry's standard dummy.</p>
  <a class="more" href="#">READ MORE...<svg width="12" height="10" viewBox="0 0 12 10"><path d="M1 1l4 4-4 4M6 1l4 4-4 4" stroke="var(--ink)" stroke-width="1.5" fill="none"/></svg></a>
</article>

<footer class="site-footer abs">
  <div class="foot-brand"><span class="mark"></span>Norvale</div>
  <span class="social" style="left:118px"></span>
  <span class="social" style="left:171px"></span>
  <span class="social" style="left:224px"></span>

  <div class="foot-col" style="left:344px">
    <h5>USEFULL LINKS</h5>
    <ul><li>» Home</li><li>» Marketing</li><li>» Sales</li><li>» News</li><li>» E-book</li></ul>
  </div>

  <div class="foot-col" style="left:610px">
    <h5>LATEST BLOG</h5>
    <div class="foot-post"><div class="ph" role="img" aria-label="Blog thumbnail" style="background:linear-gradient(135deg,#d9dee8,#8d97aa)"></div><p>Lorem Ipsum is simply dummy text of<small>Today 2:10 pm - 08.02.2017</small></p></div>
    <div class="foot-post"><div class="ph" role="img" aria-label="Blog thumbnail" style="background:linear-gradient(135deg,#c3ccd9,#6d7a90)"></div><p>Lorem Ipsum is simply dummy text of<small>Today 2:10 pm - 08.02.2017</small></p></div>
  </div>

  <div class="foot-col" style="left:873px">
    <h5>CONTACT US</h5>
    <div class="contact-row"><svg width="18" height="22" viewBox="0 0 18 22"><path d="M9 1a7 7 0 0 0-7 7c0 5 7 13 7 13s7-8 7-13a7 7 0 0 0-7-7z" stroke="#c9d2ea" stroke-width="1.5" fill="none"/><circle cx="9" cy="8" r="2.5" stroke="#c9d2ea" stroke-width="1.5" fill="none"/></svg><span>NORVALE MARKETING<br>101- Lorem Ipsum is simple dummy text of print.</span></div>
    <div class="contact-row"><svg width="18" height="18" viewBox="0 0 16 16"><path d="M3 1l3 3-2 2c1 2 3 4 5 5l2-2 3 3-2 3C7 14 2 9 1 3z" stroke="#c9d2ea" stroke-width="1.3" fill="none"/></svg><span>123-456-7890</span></div>
    <div class="contact-row"><svg width="18" height="14" viewBox="0 0 18 14"><rect x="1" y="1" width="16" height="12" stroke="#c9d2ea" stroke-width="1.5" fill="none"/><path d="M1 1l8 7 8-7" stroke="#c9d2ea" stroke-width="1.5" fill="none"/></svg><span>info@norvalemarketing.com</span></div>
  </div>

  <div class="foot-rule abs"></div>
  <p class="copyright abs">©NORVALE MARKETING - 2017 All Right Reserved</p>
</footer>

</body>
</html>
```